Lumo -Fresh business card design

It is a dry cleaning carpet business.
Red wine stain removal and pet urine treatments.
Servicing all regional areas.
Updates

all logo and pictures files have been uploaded

Industry/Entity Type

Dry Cleaning

Contact Information for Business Card

Lumo-Fresh Carpet and upholstery cleaning.
Servicing Albury/Wodonga and surrounding areas.
ph gus 0461273904 ,email lumofresh1@tealpost.example

Font styles to use
Serif
Sans Serif
Other font styles liked:
• lumo fresh logo font

Colors
ec2027
ffcf3e
33a6d7
0692cd

Requirements
Nice to have
• I have included photos of the logo and car and stripe on van ,I dont need all of them in the card just i would like to stick to these colours.

```html
<!DOCTYPE html>
<html lang="en">
<head>
<meta charset="utf-8">
<title>Lumo-Fresh Business Card</title>
<link rel="stylesheet" href="https://fonts.googleapis.com/css2?family=Russo+One&family=Exo+2:wght@300;400;500&display=swap">
<style>
  :root {
    --page-bg: #e9edf1;
    --card-white: #ffffff;
    --brand-blue: #0692cd;
    --brand-sky: #33a6d7;
    --panel-deep: #0a5fb8;
    --panel-light: #2a8ee6;
    --edge-glow: #4fb4f2;
    --ink-light: #ffffff;
    --shadow: rgba(20, 40, 70, 0.18);
  }
  * { box-sizing: border-box; margin: 0; padding: 0; }
  html, body {
    width: 1200px; height: 828px; overflow: hidden;
    background: var(--page-bg);
  }
  .sheet {
    position: relative; width: 1200px; height: 828px;
    display: flex; align-items: center; justify-content: center; gap: 60px;
  }
  .card {
    position: relative; width: 520px; height: 300px;
    background: var(--card-white);
    border-radius: 4px;
    box-shadow: 0 10px 28px var(--shadow);
    overflow: hidden;
  }
  .brand {
    position: absolute; text-align: left;
  }
  .brand-name {
    font-family: "Russo One", sans-serif;
    color: var(--brand-blue);
    letter-spacing: 1px;
    line-height: 1;
  }
  .brand-tagline {
    font-family: "Exo 2", sans-serif;
    font-weight: 500;
    color: var(--brand-sky);
    text-transform: uppercase;
    line-height: 1.1;
    text-align: center;
  }
  /* front */
  .card-front .brand { left: 50%; top: 50%; transform: translate(-50%, -50%); }
  .card-front .brand-name { font-size: 44px; }
  .card-front .brand-tagline { font-size: 17px; margin-top: 6px; }
  /* back */
  .panel { position: absolute; inset: 0; }
  .card-back .brand { left: 300px; top: 82px; }
  .card-back .brand-name { font-size: 27px; }
  .card-back .brand-tagline { font-size: 11px; margin-top: 4px; }
  .contact {
    position: absolute; left: 36px; top: 52px;
    font-family: "Exo 2", sans-serif; color: var(--ink-light);
  }
  .person-name { font-size: 15px; font-weight: 400; letter-spacing: 1px; text-transform: uppercase; }
  .person-role { font-size: 10px; font-weight: 300; margin-top: 2px; }
  .address { font-size: 12px; font-weight: 300; line-height: 1.45; margin-top: 26px; }
  .details { list-style: none; margin-top: 26px; font-size: 10px; font-weight: 300; }
  .details li { display: flex; align-items: center; gap: 8px; height: 17px; }
  .details svg { width: 10px; height: 10px; fill: none; stroke: var(--ink-light); stroke-width: 1.4; }
</style>
</head>
<body>
<main class="sheet">

  <section class="card card-front" aria-label="Card front">
    <div class="brand">
      <div class="brand-name">LUMO-FRESH</div>
      <div class="brand-tagline">Carpet &amp; Upholstery<br>Cleaning</div>
    </div>
  </section>

  <section class="card card-back" aria-label="Card back">
    <svg class="panel" viewBox="0 0 520 300" aria-hidden="true">
      <defs>
        <radialGradient id="panelFill" cx="0.6" cy="0.45" r="0.8">
          <stop offset="0" stop-color="var(--panel-light)"/>
          <stop offset="1" stop-color="var(--panel-deep)"/>
        </radialGradient>
      </defs>
      <path d="M0 0 H238 C292 80 292 220 238 300 H0 Z" fill="var(--edge-glow)"/>
      <path d="M0 0 H230 C283 80 283 220 230 300 H0 Z" fill="url(#panelFill)"/>
    </svg>

    <div class="contact">
      <div class="person-name">Dale Renwick</div>
      <div class="person-role">Managing Director</div>
      <div class="address">27 Harbour Lane<br>Kelso VIC</div>
      <ul class="details">
        <li><svg viewBox="0 0 10 10"><path d="M2 1 L4 1 L4.6 3 L3.4 4 Q4.5 6 6 6.6 L7 5.4 L9 6 L9 8 Q5 9 1 3 Z"/></svg>013 482 5571</li>
        <li><svg viewBox="0 0 10 10"><rect x="2.5" y="0.8" width="5" height="8.4" rx="1"/></svg>013 482 5571</li>
        <li><svg viewBox="0 0 10 10"><rect x="0.8" y="2" width="8.4" height="6" rx="0.6"/><path d="M1 2.4 L5 5.6 L9 2.4"/></svg>hello@lumofresh.example</li>
        <li><svg viewBox="0 0 10 10"><circle cx="5" cy="5" r="4"/><path d="M1 5 H9 M5 1 Q2.5 5 5 9 M5 1 Q7.5 5 5 9"/></svg>www.lumofresh.example</li>
      </ul>
    </div>

    <div class="brand">
      <div class="brand-name">LUMO-FRESH</div>
      <div class="brand-tagline">Carpet &amp; Upholstery<br>Cleaning</div>
    </div>
  </section>

</main>
</body>
</html>
```